Unique business card design

We are looking for a design that reflects our unique social media and online marketing agency "Kestrel Media". We are a young agency with a focus on speakers, coaches and trainers. In other words, we support people who want to do good with their work and help other people live a happier, more successful and fulfilling life, reach as many people as possible with their work and thus have an influence. Our values are: sustainability, creating added value, individuality, proactivity. We want our clients to feel comfortable with us and that's why the relationship with them is very important to us. We want every customer to become a lifelong friend of the company. Most of our clients are premium coaches, meaning they are in the higher priced segment and expect seriousness, professionalism and quality. All of these things should reflect our business card as well. I look forward to feedback. Best regards, Tomas Wylander

```html
<!DOCTYPE html>
<html lang="en">
<head>
<meta charset="utf-8">
<title>Kestrel Media – Business Card</title>
<link rel="stylesheet" href="https://fonts.googleapis.com/css2?family=Didact+Gothic&display=swap">
<style>
  :root {
    --navy: #1c1a7a;
    --deep: #14126a;
    --royal: #2b3aa8;
    --sky: #1d8fd8;
    --violet: #4a2a9a;
    --ice: #c9d8e6;
    --ink-blue: #2d3bb0;
    --grey: #9a9aa6;
    --paper: #ffffff;
    --stage: #e6e7ea;
  }
  * { box-sizing: border-box; margin: 0; padding: 0; }
  html, body { width: 1200px; height: 900px; overflow: hidden; }
  body {
    background: var(--stage);
    font-family: "Didact Gothic", "Century Gothic", sans-serif;
    display: flex;
    align-items: center;
    justify-content: center;
    gap: 80px;
  }
  .card {
    width: 480px;
    height: 480px;
    border-radius: 32px;
    overflow: hidden;
    position: relative;
    box-shadow: 0 6px 20px rgba(0,0,0,0.18);
  }

  /* Back side */
  .card-back {
    background: var(--navy);
  }
  .card-back .facets {
    position: absolute;
    inset: 0;
    background:
      linear-gradient(60deg, var(--ice) 0 12%, transparent 12%),
      linear-gradient(135deg, var(--sky) 0%, var(--royal) 35%, var(--deep) 60%, var(--violet) 80%, var(--sky) 100%);
  }
  .back-brand {
    position: absolute;
    left: 110px;
    top: 190px;
    display: flex;
    align-items: center;
    gap: 14px;
    color: var(--paper);
  }
  .back-brand .mark {
    width: 70px;
    height: 70px;
    border: 2px solid var(--paper);
  }
  .back-brand .wordmark { font-size: 34px; line-height: 1; }
  .back-brand .tagline { font-size: 14px; margin-top: 6px; letter-spacing: 0.5px; }

  /* Front side */
  .card-front {
    background: var(--paper);
  }
  .front-brand {
    position: absolute;
    left: 40px;
    top: 40px;
    display: flex;
    align-items: flex-end;
    gap: 14px;
  }
  .front-brand .mark {
    width: 84px;
    height: 84px;
    background: linear-gradient(135deg, var(--sky), var(--deep) 60%, var(--royal));
  }
  .front-brand .wordmark { font-size: 34px; line-height: 1; color: var(--navy); }
  .front-brand .tagline { font-size: 14px; color: var(--ink-blue); margin-top: 6px; }

  .person {
    position: absolute;
    left: 48px;
    top: 160px;
  }
  .person .name { font-size: 24px; color: var(--ink-blue); }
  .person .role { font-size: 21px; color: var(--grey); margin-top: 2px; }

  .contacts {
    position: absolute;
    left: 48px;
    top: 240px;
    list-style: none;
  }
  .contacts li {
    display: flex;
    align-items: center;
    gap: 10px;
    font-size: 21px;
    color: var(--ink-blue);
    line-height: 1.35;
  }
  .contacts svg { width: 18px; height: 18px; flex: none; }

  .address-band {
    position: absolute;
    left: 0;
    right: 0;
    bottom: 0;
    height: 116px;
    background: linear-gradient(100deg, var(--deep) 0%, var(--navy) 60%, var(--royal) 85%, var(--sky) 100%);
    color: var(--paper);
    padding: 24px 48px;
    font-size: 22px;
    line-height: 1.35;
  }
</style>
</head>
<body>

  <section class="card card-back" aria-label="Business card back">
    <div class="facets" role="img" aria-label="Faceted blue and violet geometric pattern"></div>
    <div class="back-brand">
      <div class="mark"></div>
      <div>
        <div class="wordmark">Kestrel Media</div>
        <div class="tagline">Online Marketing Services</div>
      </div>
    </div>
  </section>

  <section class="card card-front" aria-label="Business card front">
    <div class="front-brand">
      <div class="mark"></div>
      <div>
        <div class="wordmark">Kestrel Media</div>
        <div class="tagline">Online Marketing Services</div>
      </div>
    </div>

    <div class="person">
      <p class="name">Tomas Wylander</p>
      <p class="role">managing director</p>
    </div>

    <ul class="contacts">
      <li>
        <svg viewBox="0 0 18 18" aria-hidden="true"><rect x="1" y="1" width="16" height="16" rx="4" fill="#2d3bb0"/><path d="M5 7c0-1 1-2 4-2s4 1 4 2l-1.5 1-1-1h-3l-1 1z M6 9h6v4H6z" fill="#fff"/></svg>
        <span>5550 123 456</span>
      </li>
      <li>
        <svg viewBox="0 0 18 18" aria-hidden="true"><rect x="1" y="1" width="16" height="16" rx="4" fill="#2d3bb0"/><rect x="4" y="5.5" width="10" height="7" fill="#fff"/><path d="M4 5.5l5 4 5-4" stroke="#2d3bb0" stroke-width="1" fill="none"/></svg>
        <span>t.wylander@kestrelmedia.com</span>
      </li>
      <li>
        <svg viewBox="0 0 18 18" aria-hidden="true"><rect x="1" y="1" width="16" height="16" rx="4" fill="#2d3bb0"/><circle cx="9" cy="9" r="4.5" fill="none" stroke="#fff" stroke-width="1.2"/><path d="M4.5 9h9M9 4.5c-2 2.5-2 6.5 0 9M9 4.5c2 2.5 2 6.5 0 9" stroke="#fff" stroke-width="1" fill="none"/></svg>
        <span>www.kestrelmedia.com</span>
      </li>
    </ul>

    <div class="address-band">
      <p>48 Harbor Lane</p>
      <p>Brookfield, New York 10472</p>
    </div>
  </section>

</body>
</html>
```